Tello Haulage Junk Removal Postcard

I am looking to have a postcard made for my junk removal company. Details:
size: 6"x9"
I would like to keep it clean and simple. Our company colors are pink, blue and white. You can find the colors and info on the company and what we do on our website which is www.tellohaulage.example .
I've attached a sample of a postcard that was made on ArtHive for another junk removal company. I like the way the attached one looks.

```html
<!DOCTYPE html>
<html lang="en">
<head>
<meta charset="utf-8">
<title>Tello Haulage Postcard</title>
<link href="https://fonts.googleapis.com/css2?family=Baloo+2:wght@400;600;700;800&display=swap" rel="stylesheet">
<style>
  :root{
    --pink:#e5097f;
    --pink-soft:#e9559d;
    --blue:#1565b0;
    --white:#ffffff;
    --stage:#1e201f;
    --paper-a:#ffffff;
    --paper-b:#dcdcdd;
    --ink:#111111;
    --rule:#9a9a9a;
  }
  *{margin:0;padding:0;box-sizing:border-box}
  html,body{width:1028px;height:1200px;overflow:hidden;background:var(--stage)}
  body{position:relative;font-family:"Baloo 2",sans-serif}
  .card{position:absolute;left:140px;width:753px;height:509px;overflow:hidden;
        background:linear-gradient(160deg,var(--paper-a) 0%,#f1f1f1 40%,var(--paper-b) 100%)}
  .card--front{top:72px}
  .card--back{top:611px;height:510px}
  .card svg.shapes{position:absolute;left:0;top:0;width:100%;height:100%}
  .t{position:absolute;line-height:1;white-space:nowrap;z-index:2}
  .brand{font-weight:800;color:var(--blue);font-size:30px;display:flex;align-items:center;gap:8px}
  .brand-dot{width:14px;height:14px;border-radius:50%;background:var(--pink)}
  .social{position:absolute;display:flex;gap:5px}
  .social span{width:38px;height:38px;border-radius:50%;border:2px solid var(--blue)}
  .contact{color:var(--white);font-weight:700;font-size:18.5px}
  .headline{color:var(--white);font-weight:800;font-size:29px;line-height:1.28}
  .section-label{color:var(--pink);font-weight:700;font-size:13px}
  .rule{position:absolute;height:1px;background:var(--rule)}
  .feature{font-weight:700;font-size:13px;color:var(--ink);display:flex;align-items:center;gap:5px}
  .feature svg{width:14px;height:12px}
  .tab{color:var(--white);font-weight:700;font-size:17px}
  .service{color:var(--white);font-weight:800;font-size:30px}
  .phone-big{color:var(--white);font-weight:800;font-size:41px}
  .step{color:var(--white);font-weight:700;font-size:12.5px;text-align:center;line-height:1.3;transform:translateX(-50%)}
  .chev{color:var(--white);font-size:26px;font-weight:400;transform:translateX(-50%)}
  .photo{position:absolute;z-index:1}
  .offer{color:var(--blue);font-weight:800;font-size:35px}
  .offer em{font-style:normal;color:var(--pink)}
  .footnote{color:var(--blue);font-weight:400;font-size:15px}
  .estimate{color:var(--white);font-weight:800;font-size:38px}
  .email{color:var(--white);font-weight:700;font-size:18.5px}
  .web{color:var(--white);font-weight:800;font-size:23px}
  .stamp{position:absolute;left:643px;top:35px;width:76px;height:76px;border:1.5px solid #444}
  .addr-line{position:absolute;left:520px;width:199px;height:1px;background:#555}
</style>
</head>
<body>

<!-- Front side -->
<section class="card card--front">
  <svg class="shapes" viewBox="0 0 753 509" preserveAspectRatio="none">
    <polygon points="482,0 753,0 753,509 361,509" fill="var(--pink)"/>
    <polygon points="482,0 563,0 440,240 400,240" fill="var(--pink-soft)"/>
    <rect x="0" y="134" width="460" height="100" fill="var(--blue)"/>
    <polygon points="0,404 384,404 361,509 0,509" fill="var(--blue)"/>
    <polygon points="270,368 400,368 384,404 251,404" fill="var(--pink)"/>
  </svg>

  <div class="photo" role="img" aria-label="Photo of a white company box truck with a worker standing beside it"
       style="left:396px;top:102px;width:357px;height:324px;border-radius:6px;
              background:linear-gradient(150deg,#9fb3c6 0%,#f3f3f3 35%,#dcdcdc 60%,#2a2e36 100%)"></div>

  <div class="t brand" style="left:37px;top:48px"><span class="brand-dot"></span>Tello Haulage</div>
  <div class="social" style="left:360px;top:30px"><span></span><span></span></div>
  <div class="t contact" style="left:497px;top:21px">www.tellohaulage.example</div>
  <div class="t contact" style="left:497px;top:48px">info@tellohaulage.example</div>

  <div class="t headline" style="left:38px;top:146px">Remove the junk<br>Reclaim your space</div>

  <div class="t section-label" style="left:34px;top:245px">Why choose us?</div>
  <div class="rule" style="left:34px;top:262px;width:273px"></div>
  <div class="t feature" style="left:27px;top:272px"><svg viewBox="0 0 14 12"><path d="M1 6l4 4 8-9" fill="none" stroke="var(--blue)" stroke-width="2.4"/></svg>On time service</div>
  <div class="t feature" style="left:163px;top:272px"><svg viewBox="0 0 14 12"><path d="M1 6l4 4 8-9" fill="none" stroke="var(--blue)" stroke-width="2.4"/></svg>Upfront Pricing</div>
  <div class="t feature" style="left:27px;top:297px"><svg viewBox="0 0 14 12"><path d="M1 6l4 4 8-9" fill="none" stroke="var(--blue)" stroke-width="2.4"/></svg>Fast, Experienced</div>
  <div class="t feature" style="left:163px;top:297px"><svg viewBox="0 0 14 12"><path d="M1 6l4 4 8-9" fill="none" stroke="var(--blue)" stroke-width="2.4"/></svg>Responsible Disposal</div>

  <div class="t section-label" style="left:34px;top:327px">What we Do ?</div>
  <div class="rule" style="left:34px;top:345px;width:273px"></div>
  <div class="t feature" style="left:27px;top:355px"><svg viewBox="0 0 14 12"><path d="M1 6l4 4 8-9" fill="none" stroke="var(--blue)" stroke-width="2.4"/></svg>Residential</div>
  <div class="t feature" style="left:163px;top:355px"><svg viewBox="0 0 14 12"><path d="M1 6l4 4 8-9" fill="none" stroke="var(--blue)" stroke-width="2.4"/></svg>Commercial</div>
  <div class="t feature" style="left:27px;top:380px"><svg viewBox="0 0 14 12"><path d="M1 6l4 4 8-9" fill="none" stroke="var(--blue)" stroke-width="2.4"/></svg>Outside</div>
  <div class="t feature" style="left:163px;top:380px"><svg viewBox="0 0 14 12"><path d="M1 6l4 4 8-9" fill="none" stroke="var(--blue)" stroke-width="2.4"/></svg>Curbside</div>

  <div class="t tab" style="left:275px;top:378px">Free Estimate</div>

  <div class="t service" style="left:28px;top:412px">24/7 Customer Service</div>
  <div class="t phone-big" style="left:28px;top:448px">555-014-2290</div>

  <div class="t step" style="left:413px;top:440px">call us<br>today</div>
  <div class="t chev" style="left:455px;top:441px">&#x232A;</div>
  <div class="t step" style="left:497px;top:432px">same<br>day<br>service</div>
  <div class="t chev" style="left:538px;top:441px">&#x232A;</div>
  <div class="t step" style="left:599px;top:432px">Fast,Reliable,<br>Professional<br>Experienced</div>
  <div class="t chev" style="left:660px;top:441px">&#x232A;</div>
  <div class="t step" style="left:694px;top:440px">Best<br>Price</div>
</section>

<!-- Back side -->
<section class="card card--back">
  <svg class="shapes" viewBox="0 0 753 510" preserveAspectRatio="none">
    <polygon points="472,134 753,134 753,287 404,287" fill="var(--pink)"/>
    <polygon points="0,193 445,193 404,287 0,287" fill="var(--blue)"/>
    <polygon points="450,424 753,424 753,510 410,510" fill="var(--pink)"/>
    <polygon points="290,287 340,287 220,510 180,510" fill="var(--pink)"/>
  </svg>

  <div class="photo" role="img" aria-label="Family portrait of parents with two young children outdoors"
       style="left:0;top:287px;width:295px;height:223px;clip-path:polygon(0 0,100% 0,61% 100%,0 100%);
              background:linear-gradient(135deg,#7e8a5e 0%,#a58a73 45%,#4f5a66 100%)"></div>
  <div class="photo" role="img" aria-label="White company box truck parked on grass"
       style="left:218px;top:287px;width:218px;height:223px;clip-path:polygon(50% 0,100% 0,100% 68%,42% 100%,0 100%);
              background:linear-gradient(160deg,#3a3d44 0%,#f2f2f2 40%,#d5d5d5 70%,#8a9a5c 100%)"></div>

  <div class="t brand" style="left:31px;top:63px"><span class="brand-dot"></span>Tello Haulage</div>
  <div class="social" style="left:541px;top:35px"><span></span><span></span></div>
  <div class="stamp"></div>

  <div class="t offer" style="left:29px;top:131px">Book Today an save <em>$25</em></div>
  <div class="t footnote" style="left:29px;top:171px">* not valid on Single Item or Minimum Charge Pickups</div>

  <div class="t headline" style="left:29px;top:202px;font-size:30px">Proud To Be &nbsp;Family Owned<br>Locally Operated</div>

  <div class="t estimate" style="left:493px;top:150px">Free Estimate</div>
  <div class="rule" style="left:493px;top:193px;width:226px;height:1.5px;background:var(--white)"></div>
  <div class="t phone-big" style="left:492px;top:201px">555-014-2290</div>
  <div class="t email" style="left:489px;top:249px">info@tellohaulage.example</div>

  <div class="addr-line" style="top:318px"></div>
  <div class="addr-line" style="top:359px"></div>
  <div class="addr-line" style="top:400px"></div>

  <div class="t web" style="right:34px;top:451px">www.tellohaulage.example</div>
</section>

</body>
</html>
```